Business Cards for Corvantis LLC

We need business cards for a new company called “Corvantis LLC”. This is a technology process improvement company providing a comprehensive assessment of the technology used to run their business. The documentation and review process delivers the visibility and reassurance they need to protect their business and plan for the future. The product is called “Halvorne Ledgerwork”. Our primary target is small-medium size businesses, with the deliverables going to the decision maker. We would like to see the designs use the color blue. Our tag line is PROTECT YOUR BUSINESS · TAKE CONTROL OF IT.

Industry/Entity Type

Business

Contact Information for Business Card

Tag line should be on back of card - it does not have to be upper case.

Requirements
Must have
• Please use information when laying out card:
• Name: Darnell Pruitt
• Title: Partner
• Phone Number: (877)555-0143
• Email: dell@corvantisllc.com
• Website: http://corvantisllc.com

```html
<!DOCTYPE html>
<html lang="en">
<head>
<meta charset="utf-8">
<title>Corvantis LLC — Business Cards</title>
<link rel="stylesheet" href="https://fonts.googleapis.com/css2?family=Montserrat:wght@300;400;700&display=swap">
<style>
  :root {
    --canvas-bg: #e8e9eb;
    --card-dark: #0f1428;
    --card-light: #ffffff;
    --brand-blue: #0a76be;
    --text-white: #ffffff;
    --text-grey: #7a7d85;
    --rule-grey: #8d909c;
  }
  * { margin: 0; padding: 0; box-sizing: border-box; }
  html, body {
    width: 1200px;
    height: 1000px;
    overflow: hidden;
  }
  body {
    position: relative;
    background: var(--canvas-bg);
    font-family: "Montserrat", Arial, sans-serif;
  }
  .card {
    position: absolute;
    width: 526px;
    height: 300px;
  }
  .card--front {
    left: 181px;
    top: 176px;
    background: var(--card-dark);
    color: var(--text-white);
  }
  .card--back {
    left: 525px;
    top: 528px;
    background: var(--card-light);
  }
  .front__brand {
    position: absolute;
    right: 26px;
    top: 74px;
    font-weight: 700;
    font-size: 26px;
    color: var(--brand-blue);
    letter-spacing: 0.5px;
  }
  .front__name {
    position: absolute;
    left: 31px;
    top: 153px;
    font-weight: 700;
    font-size: 24px;
    line-height: 1.2;
    letter-spacing: 0.2px;
    text-transform: uppercase;
  }
  .front__name-last { color: var(--brand-blue); }
  .front__role {
    position: absolute;
    left: 29px;
    top: 182px;
    display: flex;
    align-items: center;
    font-weight: 300;
  }
  .front__title { font-size: 19px; }
  .front__divider {
    width: 1px;
    height: 18px;
    background: var(--rule-grey);
    margin: 0 10px;
  }
  .front__phone { font-size: 14px; font-weight: 400; }
  .front__rule {
    position: absolute;
    left: 26px;
    right: 26px;
    top: 229px;
    height: 1px;
    background: var(--rule-grey);
  }
  .contact {
    position: absolute;
    top: 251px;
    display: flex;
    align-items: center;
    gap: 4px;
    font-size: 14px;
    font-weight: 400;
  }
  .contact--email { left: 29px; }
  .contact--web { right: 26px; }
  .contact__icon { width: 18px; height: 18px; display: block; }
  .back__brand {
    position: absolute;
    left: 0;
    right: 0;
    top: 160px;
    text-align: center;
    font-weight: 700;
    font-size: 34px;
    line-height: 1.2;
    color: var(--brand-blue);
    letter-spacing: 1px;
  }
  .back__tagline {
    position: absolute;
    left: 0;
    right: 0;
    top: 212px;
    text-align: center;
    font-weight: 400;
    font-size: 13px;
    color: var(--text-grey);
    letter-spacing: 0.5px;
  }
</style>
</head>
<body>
  <section class="card card--front" aria-label="Business card front">
    <div class="front__brand">Corvantis</div>
    <h1 class="front__name">Darnell <span class="front__name-last">Pruitt</span></h1>
    <div class="front__role">
      <span class="front__title">Partner</span>
      <span class="front__divider"></span>
      <span class="front__phone">(877)555-0143</span>
    </div>
    <div class="front__rule"></div>
    <div class="contact contact--email">
      <svg class="contact__icon" viewBox="0 0 18 18" aria-hidden="true">
        <circle cx="9" cy="9" r="9" fill="#ffffff"/>
        <rect x="4.5" y="5.8" width="9" height="6.4" rx="0.8" fill="#0f1428"/>
        <path d="M4.8 6.2 L9 9.3 L13.2 6.2" fill="none" stroke="#ffffff" stroke-width="0.9"/>
      </svg>
      <span>dell@corvantisllc.com</span>
    </div>
    <div class="contact contact--web">
      <svg class="contact__icon" viewBox="0 0 18 18" aria-hidden="true">
        <circle cx="9" cy="9" r="9" fill="#ffffff"/>
        <g fill="none" stroke="#0f1428" stroke-width="1">
          <circle cx="9" cy="9" r="5"/>
          <ellipse cx="9" cy="9" rx="2.2" ry="5"/>
          <line x1="4" y1="9" x2="14" y2="9"/>
          <line x1="4.8" y1="6.5" x2="13.2" y2="6.5"/>
          <line x1="4.8" y1="11.5" x2="13.2" y2="11.5"/>
        </g>
      </svg>
      <span>www.corvantisllc.com</span>
    </div>
  </section>

  <section class="card card--back" aria-label="Business card back">
    <div class="back__brand">Corvantis LLC</div>
    <p class="back__tagline">Protect your business · Take control of IT</p>
  </section>
</body>
</html>
```